Medical Device Design Firm- needs a new Web design

Background: Our company CorvanWorks - corvanworks.com, is a engineering firm that focuses on designing medical devices for established medical companies and start ups. We have mechanical, electrical, software, prototyping and mfg services.

Need: We need a website design that portrays "medical" descriptions like: clean, sterile, quality, precision, experts, world class

Photos: We can provide high end photos-realistic renderings of products we have designed. We also look to have doctors and patients using products we have designed.
Updates

Hi All,

Please use pictures on our existing website for now. www.corvanworks.com. Same with the logo.

Also, the contest is "guaranteed" for payment now.

Best,
Ti

Reason: We are trying to get feedback on the designs from our team. Therefore we would like to extend the deadline for further feedback and decisions. Thx Ti

Target Market(s)

medical mfg companies: exectutives, vp marketing, r&d directors, engineers, start-up companies, strategic partners

Industry/Entity Type

Medical

Requirements
Must have
• * Must be coded for Wordpress
* Home page
- includes large splash banner
- main description
- news column
- top section: telephone #, contact

* Our Work (portfolio page)
- Large photos

* Services Page

• Industrial Design
• Mechanical Engineering
• Electronics and Software
• Prototyping and Manufacturing
• Concept to Market
• Medical Carts

* Case Studies Page

{websites we like}
http://pebblemedtech.com/
http://www.quillonmedicaldesignhub.com/
http://www.vantrelpd.com/

Nice to have
• http://www.vantrelpd.com/
The splash banner expands to outside area as viewed on wide monitors.

```html
<!DOCTYPE html>
<html lang="en">
<head>
<meta charset="utf-8">
<title>CorvanWorks – Medical Product Design</title>
<link rel="stylesheet" href="https://fonts.googleapis.com/css2?family=Play:wght@400;700&family=Open+Sans:wght@400;600;700&display=swap">
<style>
:root{
  --accent:#b04a0c;
  --accent-dark:#8f3a08;
  --ink:#2b2b2b;
  --text:#444;
  --muted:#777;
  --line:#d9d9d9;
  --band:#efefef;
  --paper:#fff;
  --social:#3b77c6;
}
*{box-sizing:border-box;margin:0;padding:0}
html,body{width:715px;height:1200px;overflow:hidden;background:var(--paper)}
body{position:relative;font-family:"Open Sans",Arial,sans-serif;color:var(--text);font-size:8px;line-height:1.6}
.head-font{font-family:"Play","Trebuchet MS",sans-serif}
.topbar{position:absolute;top:0;left:0;width:715px;height:4px;background:var(--accent-dark)}
.brand{position:absolute;left:27px;top:38px;display:flex;align-items:center;gap:8px}
.brand-mark{width:18px;height:18px;border-radius:50%;background:var(--accent)}
.brand-name{font-family:"Play",sans-serif;font-size:27px;color:var(--ink);letter-spacing:-.5px}
.contact-line{position:absolute;right:27px;top:20px;display:flex;align-items:center;gap:4px;font-family:"Play",sans-serif;font-size:15px;color:var(--ink)}
.social{width:14px;height:14px;background:var(--social);border-radius:2px}
.contact-line .area{color:var(--accent);margin-left:6px}
.main-nav{position:absolute;right:27px;top:63px;display:flex;font-family:"Play",sans-serif;font-size:12px;color:var(--accent)}
.main-nav span{padding:0 14px;border-left:1px solid var(--accent);line-height:13px}
.main-nav span:first-child{border-left:0}
.main-nav span:last-child{padding-right:0}
.hero-band{position:absolute;top:88px;left:0;width:715px;height:280px;background:linear-gradient(#f7f7f7,var(--band))}
.hero{position:absolute;left:18px;top:95px;width:674px;height:246px;background:var(--paper);border:1px solid #ddd;box-shadow:0 10px 12px -8px rgba(0,0,0,.35)}
.hero h1{position:absolute;left:51px;top:38px;font-family:"Play",sans-serif;font-weight:400;font-size:22px;color:var(--ink)}
.hero h2{position:absolute;left:51px;top:66px;font-family:"Play",sans-serif;font-weight:400;font-size:15px;color:var(--accent)}
.hero p{position:absolute;left:51px;top:92px;width:250px;font-size:7px;line-height:1.75;color:var(--accent)}
.btn{position:absolute;left:51px;top:155px;background:var(--accent);color:#fff;font-family:"Play",sans-serif;font-size:11px;padding:4px 10px;border-radius:2px}
.hero-visual{position:absolute;left:375px;top:10px;width:270px;height:226px;background:linear-gradient(135deg,#dfe3ef,#8b95bf 55,#e8e8ea);background:linear-gradient(135deg,#e4e7f0,#9aa3c8 55%,#e6e6e8)}
.arrow{position:absolute;top:195px;width:22px;height:30px;background:var(--accent);display:flex;align-items:center;justify-content:center}
.arrow.left{left:18px;border-radius:0 15px 15px 0;left:16px}
.arrow.right{right:16px;border-radius:15px 0 0 15px}
.section-title{position:absolute;font-family:"Play",sans-serif;font-weight:400;color:var(--ink)}
.services{position:absolute;top:0;left:0}
.service{position:absolute;width:330px}
.service .thumb{position:absolute;left:0;top:0;width:83px;height:65px;border:1px solid #ccc;border-radius:3px;background:linear-gradient(#f3f3f3,#d6d6d6)}
.service h3{position:absolute;left:91px;top:-3px;font-family:"Play",sans-serif;font-weight:400;font-size:13px;color:var(--accent)}
.service p{position:absolute;left:91px;top:17px;width:230px;font-size:7px;line-height:1.75;color:var(--text)}
.work{position:absolute;top:637px;width:111px}
.work .thumb{width:111px;height:76px;border:1px solid #ccc;border-radius:3px;padding:3px;background:var(--paper)}
.work .thumb div{width:100%;height:100%}
.work p{margin-top:16px;font-family:"Play",sans-serif;font-size:9.5px;line-height:1.45;color:var(--ink)}
.chev{position:absolute;top:662px;font-size:26px;color:#bbb;font-family:"Play",sans-serif}
.rule{position:absolute;left:21px;width:675px;height:1px;background:var(--line)}
.intro h2{position:absolute;left:21px;top:798px;font-family:"Play",sans-serif;font-weight:400;font-size:13px;color:var(--accent)}
.intro p{position:absolute;left:21px;top:822px;width:680px;font-size:7.2px;line-height:1.8;color:var(--ink)}
.col-title{position:absolute;top:895px;font-family:"Play",sans-serif;font-weight:400;font-size:14px;color:var(--accent)}
.specialties{position:absolute;left:24px;top:924px;list-style:none}
.specialties li{height:17.6px;display:flex;align-items:center;gap:7px;font-size:7.4px;font-weight:600;color:var(--ink)}
.specialties li i{width:9px;height:9px;border-radius:50%;background:#eee;display:flex;align-items:center;justify-content:center;font-style:normal;font-size:6px;color:var(--muted)}
.news{position:absolute;left:379px;top:925px;width:285px}
.news time{display:block;font-size:8.5px;color:var(--ink)}
.news h4{font-family:"Play",sans-serif;font-weight:400;font-size:10px;color:var(--ink);margin-top:2px}
.news p{font-size:7.3px;line-height:1.8;color:var(--ink);margin-top:3px}
.news .more{font-size:7.5px;font-weight:700;color:var(--accent);margin-top:2px}
.news hr{border:0;border-top:1px dotted #999;margin:6px 0 8px}
.footer-band{position:absolute;top:1112px;left:0;width:715px;height:88px;background:linear-gradient(#f3f3f3,#fff 40%)}
.footer-links{position:absolute;left:0;width:715px;text-align:center;font-size:7.8px;color:var(--accent)}
.footer-links span{padding:0 5px}
.footer-links b{font-weight:400;color:var(--muted)}
.copyright{position:absolute;top:1162px;left:0;width:715px;text-align:center;font-size:7.3px;color:var(--ink)}
</style>
</head>
<body>
<div class="topbar"></div>

<header>
  <div class="brand"><span class="brand-mark"></span><span class="brand-name">CorvanWorks</span></div>
  <div class="contact-line"><span class="social"></span><span class="social"></span><span class="area">(555)</span>-318-4720</div>
  <nav class="main-nav"><span>Home</span><span>About</span><span>Services</span><span>Portfolio</span><span>News</span><span>Contact</span></nav>
</header>

<div class="hero-band"></div>
<section class="hero">
  <h1>From Concept To Marketing</h1>
  <h2>tittle line goes here</h2>
  <p>To be the best we know what and how to present beautifully the working of the client's need and their advantages be highlighted. We act in accordance with the Industry certified processes to deliver the best to our clients all over the world.</p>
  <span class="btn">view products</span>
  <div class="hero-visual" role="img" aria-label="Rendering of a large blue and white medical imaging system"></div>
</section>
<div class="arrow left"><svg width="8" height="12" viewBox="0 0 8 12"><path d="M6 1 1 6l5 5" fill="none" stroke="#fff" stroke-width="1.5"/></svg></div>
<div class="arrow right"><svg width="8" height="12" viewBox="0 0 8 12"><path d="M2 1l5 5-5 5" fill="none" stroke="#fff" stroke-width="1.5"/></svg></div>

<h2 class="section-title" style="left:30px;top:386px;font-size:15px">Medical Product Development</h2>
<div class="service" style="left:30px;top:423px">
  <div class="thumb" role="img" aria-label="Industrial design sketch of a device"></div>
  <h3>Industrial Design</h3>
  <p>To be the best we know what and how to present beautifully the working of the client's need and their advantages be highlighted.</p>
</div>
<div class="service" style="left:373px;top:423px">
  <div class="thumb" role="img" aria-label="Electronics circuit schematic" style="background:linear-gradient(#fafafa,#e9e4f0)"></div>
  <h3>Electronics and Software</h3>
  <p>To be the best we know what and how to present beautifully the working of the client's need and their advantages be highlighted.</p>
</div>
<div class="service" style="left:30px;top:507px">
  <div class="thumb" role="img" aria-label="Mechanical engineering rendering of a purple instrument" style="background:linear-gradient(135deg,#f3f3f6,#5a5cb8)"></div>
  <h3>Mechanical Engineering</h3>
  <p>To be the best we know what and how to present beautifully the working of the client's need and their advantages be highlighted.</p>
</div>
<div class="service" style="left:373px;top:507px">
  <div class="thumb" role="img" aria-label="Prototype medical workstation on a cart" style="background:linear-gradient(#f2f2f2,#c9ccd2)"></div>
  <h3>Prototyping and Manufacturing</h3>
  <p>To be the best we know what and how to present beautifully the working of the client's need and their advantages be highlighted.</p>
</div>

<span class="chev" style="left:12px">&#10094;</span>
<span class="chev" style="left:678px">&#10095;</span>
<div class="work" style="left:35px"><div class="thumb"><div role="img" aria-label="Ophthalmic laser cart" style="background:linear-gradient(#eef0f4,#9aa0ab)"></div></div><p>Ophthalmic Laser Cart for Top-Tier Company</p></div>
<div class="work" style="left:166px"><div class="thumb"><div role="img" aria-label="Prostate imaging system" style="background:linear-gradient(#2a2a2a,#0e0e0e)"></div></div><p>Prostate Imaging System</p></div>
<div class="work" style="left:297px"><div class="thumb"><div role="img" aria-label="Handheld forensic device" style="background:linear-gradient(#fff,#ececec)"></div></div><p>Handheld Forensic Device</p></div>
<div class="work" style="left:429px"><div class="thumb"><div role="img" aria-label="Immunoassay diagnostic bench top system" style="background:linear-gradient(#e8e8e8,#a8a8a8)"></div></div><p>Immunoassay Diagnostic Bench Top System</p></div>
<div class="work" style="left:559px"><div class="thumb"><div role="img" aria-label="Handheld electronic baseball counter" style="background:radial-gradient(circle,#3a3a3a 35%,#fff 60%)"></div></div><p>Handheld Electronic Base-ball Counter</p></div>

<div class="rule" style="top:780px"></div>

<section class="intro">
  <h2>Medical Cart, Equipment, Instrument and Medical Device Industrial Design</h2>
  <p>CorvanWorks is a contract medical device design and product development firm. We are a full service company for mechanical engineering, electronics, software, industrial design, prototyping, manufacturing, FDA regulatory consulting and product testing services. Expertise includes medical user interface (UI) design, custom medical cart development, medical device, industrial design, hospital equipment and lab instrument development. Based in Orange County, CA, we serve Southern California (San Diego through Los Angeles) and medical device firms nationwide. Contact CorvanWorks to take your product from concept to market.</p>
</section>

<h2 class="col-title" style="left:21px">Our Specialties</h2>
<ul class="specialties">
  <li><i>&#8250;</i>Handheld Medical Device and Surgical Instrument Design</li>
  <li><i>&#8250;</i>Disposable Medical Device Development</li>
  <li><i>&#8250;</i>Advanced Medical Equipment and Systems Engineering Services</li>
  <li><i>&#8250;</i>Clinical/Biotech Lab Equipment Development (bench-top/tabletop instruments)</li>
  <li><i>&#8250;</i>Therapeutic, Diagnostic and Patient Monitoring Equipment Development</li>
  <li><i>&#8250;</i>FDA Class 1, Class II device testing and regulatory consulting</li>
  <li><i>&#8250;</i>Medical Cart Development and Custom, POC, Mobile Cart Design</li>
  <li><i>&#8250;</i>Medical Device Design</li>
  <li><i>&#8250;</i>Laboratory Equipment Design</li>
</ul>

<h2 class="col-title" style="left:379px">Latest News &amp; Updates</h2>
<section class="news" style="top:925px">
  <article>
    <time>20.March.2012</time>
    <h4>Certified processes to deliver the best to our clients</h4>
    <p>To be the best we know what and how to present beautifully the working of the client's need and their advantages be highlighted.</p>
    <div class="more">read more &#8250;</div>
  </article>
  <hr>
  <article>
    <time>10.March.2012</time>
    <h4>Certified processes to deliver the best to our clients</h4>
    <p>We at Brightmere Studio think graphic design as a combination and collaboration of ideas and technology. We can assure you that this is the best place for requirement of yours regarding website design solutions</p>
    <div class="more">read more &#8250;</div>
  </article>
</section>

<footer>
  <div class="footer-band"></div>
  <div class="footer-links" style="top:1126px"><span>Home</span><b>|</b><span>About</span><b>|</b><span>Portfolio</span><b>|</b><span>Services</span><b>|</b><span>Engineering</span><b>|</b><span>Electronics and Software</span><b>|</b><span>Design</span><b>|</b><span>Prototyping and Manufacturing</span></div>
  <div class="footer-links" style="top:1139px"><span>Full Service</span><b>|</b><span>Medical Device Development</span><b>|</b><span>Medical Carts</span><b>|</b><span>Sitemap</span><b>|</b><span>Contact</span></div>
  <div class="copyright">© 2012 A Medical Product Design Firm &nbsp;|&nbsp; All right reserved &nbsp;|&nbsp; Term &amp; Conditions</div>
</footer>
</body>
</html>
```